Christmas Banner for frontpage of website

New online scarf store just opened needs a Christmas Banner stating Free Delivery (UK only). Also if it could incorporate guaranteed Christmas delivery if ordered before 18th (might be too wordy though?) I would really like it to bring some colour to the page. The page is currently black and white with a pink accent and is very simple which is why I would like something modern and elegant, simple but with some colour. It is a shopify store I understand the banner size should be 950px by 290px the website is www.velmorrow.co.uk

Target Market(s)

Ladies

Industry/Entity Type

Store

Requirements
Should not have
• Not to look tacky.

```html
<!DOCTYPE html>
<html lang="en">
<head>
<meta charset="utf-8">
<title>Velmorrow – Christmas Banner</title>
<link href="https://fonts.googleapis.com/css2?family=Great+Vibes&family=Dancing+Script:wght@500&family=Annie+Use+Your+Telescope&display=swap" rel="stylesheet">
<style>
  :root {
    --snow-light: #f4f8fb;
    --snow-mid: #dfe9f1;
    --snow-blue: #c3d6e4;
    --scarf-teal: #2fa5b0;
    --scarf-deep: #1d7f89;
    --brand-red: #c3373f;
    --accent-red: #cf4a52;
    --ink: #2b2b2b;
  }
  html, body {
    margin: 0;
    padding: 0;
    overflow: hidden;
    background: #ffffff;
  }
  .banner {
    position: relative;
    width: 1200px;
    height: 366px;
    overflow: hidden;
  }
  .banner__backdrop {
    position: absolute;
    inset: 0;
    background:
      radial-gradient(circle at 15% 15%, rgba(255,255,255,0.9) 0, rgba(255,255,255,0) 30%),
      radial-gradient(circle at 40% 85%, rgba(255,255,255,0.7) 0, rgba(255,255,255,0) 28%),
      linear-gradient(160deg, var(--snow-light) 0%, var(--snow-mid) 55%, var(--snow-blue) 100%);
  }
  .banner__photo {
    position: absolute;
    top: 0;
    right: 0;
    width: 560px;
    height: 366px;
    background: linear-gradient(90deg,
      rgba(195,214,228,0) 0%,
      rgba(47,165,176,0.45) 25%,
      var(--scarf-teal) 55%,
      var(--scarf-deep) 100%);
  }
  .banner__copy {
    position: absolute;
    left: 0;
    top: 0;
    width: 680px;
    height: 366px;
  }
  .brand-name {
    position: absolute;
    left: 38px;
    top: 6px;
    margin: 0;
    font-family: "Great Vibes", cursive;
    font-weight: 400;
    font-size: 128px;
    line-height: 1.35;
    color: var(--brand-red);
    white-space: nowrap;
  }
  .offer {
    position: absolute;
    left: 52px;
    top: 168px;
    margin: 0;
    font-family: "Dancing Script", cursive;
    font-weight: 500;
    font-size: 44px;
    line-height: 1;
    color: var(--accent-red);
    white-space: nowrap;
  }
  .offer__note {
    font-size: 28px;
  }
  .offer-icon {
    position: absolute;
    left: 418px;
    top: 172px;
    width: 44px;
    height: 44px;
  }
  .offer-underline {
    position: absolute;
    left: 40px;
    top: 210px;
    width: 580px;
    height: 26px;
  }
  .deadline {
    position: absolute;
    left: 43px;
    top: 240px;
    margin: 0;
    font-family: "Annie Use Your Telescope", cursive;
    font-size: 34px;
    line-height: 1;
    color: var(--ink);
    white-space: nowrap;
  }
  .divider {
    position: absolute;
    left: 140px;
    top: 302px;
    width: 480px;
    height: 30px;
  }
</style>
</head>
<body>
<div class="banner">
  <div class="banner__backdrop" role="img" aria-label="Soft snowy background with sparkling winter bokeh"></div>
  <div class="banner__photo" role="img" aria-label="Photo of a white rabbit wrapped in a teal knitted scarf"></div>

  <div class="banner__copy">
    <h1 class="brand-name">Velmorrow</h1>

    <p class="offer">Free Delivery <span class="offer__note">(UK only)</span></p>

    <svg class="offer-icon" viewBox="0 0 40 40" aria-hidden="true">
      <g stroke="var(--accent-red)" stroke-width="3" stroke-linecap="round">
        <line x1="20" y1="3" x2="20" y2="37"/>
        <line x1="5.3" y1="11.5" x2="34.7" y2="28.5"/>
        <line x1="5.3" y1="28.5" x2="34.7" y2="11.5"/>
      </g>
    </svg>

    <svg class="offer-underline" viewBox="0 0 580 26" aria-hidden="true">
      <path d="M4 8 C 20 22, 40 22, 60 14 S 260 10, 576 12" fill="none" stroke="var(--accent-red)" stroke-width="2.2" stroke-linecap="round"/>
    </svg>

    <p class="deadline">Guaranteed Christmas delivery if ordered before 18th</p>

    <svg class="divider" viewBox="0 0 480 30" aria-hidden="true">
      <line x1="0" y1="15" x2="215" y2="15" stroke="var(--accent-red)" stroke-width="2"/>
      <line x1="265" y1="15" x2="480" y2="15" stroke="var(--accent-red)" stroke-width="2"/>
      <polygon points="240,3 243.5,11.5 252.5,11.8 245.5,17.5 248,26.5 240,21.3 232,26.5 234.5,17.5 227.5,11.8 236.5,11.5" fill="var(--accent-red)"/>
    </svg>
  </div>
</div>
</body>
</html>
```